Exciting new aperitif brand needs a great label

Vel-Doro is a wonderful rich new premium-priced bitter aperitif, with a deep red colour, from a 100+ year old distillery (1890) near Turin in the Piedmont region of Italy. Inspired by Tessoli, it is perfectly formulated to elevate the classic Negroni cocktail (and variations on it). It also goes perfectly in a Spritz or a long mixed drink with soda or tonic. The name Vel-Doro is derived from the French for 'peak' and the Italian word for 'love'.

The label, which should take inspiration from Tessoli, but be distinctively different, can incoporate any number of premium label embellishments (foil, embossing, textures etc) and should be no greater than 11cm (height) x 9cm (width) with any core imagery restricted to a width of c.7cm.

The attached mood board should act as inspiration and colour should largely be restricted to reds, blues, whites and perhaps orange. For completeness, the label should note that the ABV is 25% and the bottle size 70cl.

Target Market(s)

21-45yr olds - equal split female/male

Colors
0054AA
0677BA
7BADD7
CADEEF
E8F1F8
0094D4
00A9DD
6FCCEA
C7EBF8
E9F6FB
EE7325
F08F49
F5BC92
FAE3D3
FDF4ED
EB3D1F
EC4F4E
F09395
F8D3D4
FCEDEE

Requirements
Must have
• Great lettering design on the name Vel-Doro

```html
<!DOCTYPE html>
<html lang="en">
<head>
<meta charset="utf-8">
<title>Vel-Doro Bitter Label</title>
<link rel="stylesheet" href="https://fonts.googleapis.com/css2?family=Alfa+Slab+One&family=Mrs+Saint+Delafield&family=Playfair+Display:wght@400&family=Raleway:wght@300;700&display=swap">
<style>
  :root {
    --navy: #0f1b3b;
    --gold-dark: #7a3d05;
    --gold-mid: #c98a1a;
    --gold-light: #ffe27a;
    --gold-pale: #fff6c8;
    --ink-white: #ececec;
    --peak-grey: #7b8388;
    --peak-snow: #c8d5da;
    --page: #ffffff;
    --gold-sheen: linear-gradient(90deg, var(--gold-light) 0%, var(--gold-pale) 25%, var(--gold-mid) 55%, var(--gold-light) 75%, var(--gold-dark) 100%);
  }
  * { box-sizing: border-box; margin: 0; padding: 0; }
  html, body { width: 1200px; height: 1200px; overflow: hidden; background: var(--page); }
  .canvas { position: relative; width: 1200px; height: 1200px; }

  .label-frame {
    position: absolute; left: 220px; top: 150px; width: 760px; height: 960px;
    background: var(--gold-sheen);
  }
  .label-panel {
    position: absolute; inset: 22px; background: var(--navy);
  }
  .peaks-art {
    position: absolute; left: 0; top: 0; right: 0; height: 372px;
    background: linear-gradient(180deg, var(--navy) 0%, var(--navy) 12%, var(--peak-snow) 30%, var(--peak-grey) 70%, #8c9397 100%);
  }

  .name-band {
    position: absolute; left: 160px; top: 544px; width: 880px; height: 260px;
    background: var(--gold-sheen);
  }
  .name-band-inner {
    position: absolute; inset: 22px; background: var(--navy);
    display: flex; align-items: center; justify-content: center; gap: 22px;
  }
  .brand-name {
    font-family: "Alfa Slab One", Georgia, serif;
    font-size: 128px; line-height: 1; color: var(--ink-white);
    letter-spacing: 2px;
  }
  .brand-dot {
    width: 26px; height: 26px; border-radius: 50%; background: var(--ink-white);
  }

  .heritage {
    position: absolute; left: 220px; top: 830px; width: 760px; text-align: center;
  }
  .heritage-since {
    font-family: "Mrs Saint Delafield", cursive; font-size: 48px; color: var(--ink-white);
    line-height: 1; display: block;
  }
  .heritage-year {
    font-family: "Playfair Display", Georgia, serif; font-size: 78px; line-height: 1;
    color: var(--gold-mid); display: block; margin-top: -6px;
  }
  .heritage-region {
    font-family: "Mrs Saint Delafield", cursive; font-size: 60px; color: var(--ink-white);
    line-height: 1; display: block; margin-top: -22px;
  }

  .spec-row {
    position: absolute; left: 242px; top: 1036px; width: 716px;
    display: flex; justify-content: space-around; align-items: center;
    font-family: "Raleway", Arial, sans-serif; font-size: 27px; color: var(--ink-white);
  }
  .spec-abv, .spec-volume { font-weight: 300; }
  .spec-type { font-weight: 700; color: var(--gold-mid); letter-spacing: 1px; }
</style>
</head>
<body>
<main class="canvas">
  <section class="label-frame">
    <div class="label-panel">
      <div class="peaks-art" role="img" aria-label="Illustration of snow-capped alpine mountain peaks"></div>
    </div>
  </section>

  <header class="name-band">
    <div class="name-band-inner">
      <span class="brand-name">VEL</span>
      <span class="brand-dot"></span>
      <span class="brand-name">DORO</span>
    </div>
  </header>

  <div class="heritage">
    <span class="heritage-since">since</span>
    <span class="heritage-year">1890</span>
    <span class="heritage-region">Piedmont</span>
  </div>

  <footer class="spec-row">
    <span class="spec-abv">25% ABV</span>
    <span class="spec-type">BITTER</span>
    <span class="spec-volume">700ML</span>
  </footer>
</main>
</body>
</html>
```